2016 Spring tune up

We sell automatic pool covers. We need a postcard design for a mailer to be sent to our customers about a yearly tune up , also offering a discount for a fabric replacement for their automatic pool cover system. The attached information and pictures should be included on the postcard. We would like to see designs that include the colors in our address label

Target Market(s)

Current Automatic Pool Cover Owners

Requirements
Must have
• www.mdrvk.com
• Contact info-service@mdrvk.com
• Attached images and documents
Nice to have
• Color match to our attached logo
Should not have
• Should not have pictures with pools without covers.

```html
<!DOCTYPE html>
<html lang="en">
<head>
<meta charset="utf-8">
<title>Spring Tune Up Postcard</title>
<link rel="stylesheet" href="https://fonts.googleapis.com/css2?family=PT+Sans:ital,wght@0,400;0,700;1,700&family=Oswald:wght@500&family=Carlito:wght@400&family=Tinos&display=swap">
<style>
  :root{
    --backdrop:#5e5e5e;
    --paper:#ffffff;
    --navy:#0b4f9c;
    --brand-blue:#0a5aa6;
    --sky:#1ea6e2;
    --ink:#1a1a1a;
    --rule:#8a8a8a;
    --yellow:#f6e81c;
    --photo-sky:#2f7fd6;
    --photo-sea:#3aa0d8;
    --photo-deck:#e9ebea;
  }
  *{box-sizing:border-box;margin:0;padding:0}
  html,body{width:1200px;height:975px;overflow:hidden}
  body{background:var(--backdrop);position:relative;font-family:"Carlito","Calibri",sans-serif;color:var(--ink)}
  .postcard{position:absolute;left:80px;top:85px;width:1040px;height:803px;background:var(--paper)}
  .headline{position:absolute;left:40px;top:32px;font-family:"PT Sans",sans-serif;font-weight:700;font-size:54px;line-height:54px;color:var(--navy);letter-spacing:-0.3px}
  .headline .accent{color:var(--sky)}
  .hero{position:absolute;left:41px;top:158px;width:649px;height:364px;overflow:hidden}
  .hero-photo{position:absolute;inset:0;background:linear-gradient(180deg,var(--photo-sky) 0%,#7fb8ec 48%,var(--photo-sea) 52%,#1f6fb8 78%,var(--photo-deck) 92%)}
  .hero-offer{position:absolute;left:24px;top:20px;font-family:"PT Sans",sans-serif;font-style:italic;font-weight:700;font-size:29px;line-height:35px;color:#fff;text-transform:uppercase;letter-spacing:-0.5px}
  .hero-offer .hl{color:var(--yellow)}
  .brand-tag{position:absolute;left:17px;top:264px;width:258px;height:77px;background:#fff;padding:6px}
  .brand-tag .name{font-family:"PT Sans",sans-serif;font-weight:700;font-size:21px;line-height:30px;color:var(--brand-blue);text-align:center;padding-top:14px}
  .prices{position:absolute;top:536px;left:41px;width:649px;height:126px}
  .price{position:absolute;top:0;height:126px;background:var(--brand-blue);color:#fff;text-align:center;font-family:"Oswald",sans-serif;font-weight:500;text-transform:uppercase}
  .price .label{font-size:23px;line-height:29px;padding-top:12px}
  .price .amount{font-size:36px;line-height:44px;margin-top:8px}
  .price.basic{left:0;width:227px}
  .price.mechanical{left:237px;width:217px}
  .price.deluxe{left:469px;width:180px}
  .fine-print{position:absolute;left:41px;top:673px;width:660px;font-family:"Tinos",serif;font-size:14.5px;line-height:16px;color:#333}
  .services{position:absolute;left:705px;top:36px;width:312px}
  .service{margin-bottom:16px}
  .service h2{font-family:"PT Sans",sans-serif;font-weight:700;font-size:19px;line-height:24px;color:var(--brand-blue);border-bottom:1px solid var(--rule);padding-bottom:1px;width:290px;display:flex;align-items:center;gap:8px}
  .service h2 svg{flex:none}
  .service p{font-size:18.5px;line-height:24px;padding-left:24px;margin-top:5px;color:var(--ink)}
  .service .note{font-size:13px;line-height:18px;display:block}
  .divider{position:absolute;left:48px;right:40px;top:728px;border-top:1px solid var(--rule)}
  .contact{position:absolute;left:50px;top:745px;display:flex;align-items:center;gap:14px;font-family:"PT Sans",sans-serif;font-weight:700;font-size:26px;color:var(--sky)}
  .contact .lead{color:#1f3f8f;font-size:25px}
  .contact svg{flex:none}
</style>
</head>
<body>
<main class="postcard">
  <h1 class="headline">We are offering our<br>yearly <span class="accent">tune up specials</span></h1>

  <section class="hero">
    <div class="hero-photo" role="img" aria-label="Photo of a lakeside pool with an automatic cover, trees and blue sky"></div>
    <p class="hero-offer"><span class="hl">20% off</span> fabric<br>replacement and spring<br><span class="hl">tune up specials</span></p>
    <div class="brand-tag"><p class="name">Northshore Automatic Pool Covers</p></div>
  </section>

  <section class="prices">
    <div class="price basic"><p class="label">Basic cover cleaning<br>starting at</p><p class="amount">$290.00</p></div>
    <div class="price mechanical"><p class="label">Mechanical tune up<br>starting at</p><p class="amount">$330.00</p></div>
    <div class="price deluxe"><p class="label">Deluxe tune up<br>starting at</p><p class="amount">$495.00</p></div>
  </section>

  <p class="fine-print">Prepay fabric replacement or spring tune up by April 15, 2016 and receive a 20% discount or by April 30, 2016 and receive a 10% discount. (Vanishing/stone lids extra) {Please call for details}</p>

  <section class="services">
    <article class="service">
      <h2><svg width="12" height="14" viewBox="0 0 12 14"><path d="M1 1l9 6-9 6 3-6z" fill="var(--sky)"/></svg>Basic Cover Cleaning includes</h2>
      <p>Cleaning of the top of the cover only (up to 2 hours of labor included)<span class="note">{Does not include adjustments/lubrication}</span></p>
    </article>
    <article class="service">
      <h2><svg width="12" height="14" viewBox="0 0 12 14"><path d="M1 1l9 6-9 6 3-6z" fill="var(--sky)"/></svg>Mechanical tune up includes</h2>
      <p>Removal of debris and cleaning of recessed housing or bench enclosure, lubrication, inspection of all moving parts, tightening track, and making adjustments for proper operation (up to2 hours of labor included) Replacement of End Casting Pulleys to help prevent premature rope breakage<span class="note">{DOES NOT include cleaning of fabric}</span></p>
    </article>
    <article class="service">
      <h2><svg width="12" height="14" viewBox="0 0 12 14"><path d="M1 1l9 6-9 6 3-6z" fill="var(--sky)"/></svg>Deluxe tune up includes</h2>
      <p>All of the services provided in the basic cover cleaning and Mechanical tune up plus: Replacement of gliders (on under track units only), guides and shear bolt or pin.<br>(up to 3 hours of labor included)</p>
    </article>
  </section>

  <div class="divider"></div>
  <footer class="contact">
    <span class="lead">For Details Contact</span>
    <svg width="12" height="14" viewBox="0 0 12 14"><path d="M1 1l9 6-9 6 3-6z" fill="var(--navy)"/></svg>
    <span>800-555-0147</span>
    <svg width="12" height="14" viewBox="0 0 12 14"><path d="M1 1l9 6-9 6 3-6z" fill="var(--navy)"/></svg>
    <span>service@mdrvk.com</span>
    <svg width="12" height="14" viewBox="0 0 12 14"><path d="M1 1l9 6-9 6 3-6z" fill="var(--navy)"/></svg>
    <span>www.mdrvk.com</span>
  </footer>
</main>
</body>
</html>
```